Poster

I have an animal hospital. I want a poster to hang in each exam room to show a picture of a normal sized heart and then an enlarged heart of a dog that was fed a grain-free diet. I want to warn people not to feed grain-free diets. Maybe at the top of the poster, "Do you feed grain-free?" and then the x-ray comparison, then the warnings of Canine Dilated Cardiomyopathy.

```html
<!DOCTYPE html>
<html lang="en">
<head>
<meta charset="utf-8">
<title>Do you feed grain-free? – DCM warning poster</title>
<link href="https://fonts.googleapis.com/css2?family=Montserrat:wght@400;600;700&family=Rubik+Dirt&family=Kaushan+Script&display=swap" rel="stylesheet">
<style>
  :root{
    --orange:#f6a31b;
    --ink:#2f2f2f;
    --brown:#8c6a30;
    --text:#222;
    --soft-grey:#ececec;
    --paper:#ffffff;
    --chain:#8a8a8a;
  }
  *{margin:0;padding:0;box-sizing:border-box}
  html,body{width:848px;height:1200px;overflow:hidden;background:var(--paper)}
  .poster{
    position:relative;width:848px;height:1200px;overflow:hidden;
    background:radial-gradient(ellipse at 85% 85%, #ececec 0%, #f7f7f7 35%, #ffffff 65%);
    font-family:'Montserrat',sans-serif;color:var(--text);
  }
  .backdrop{position:absolute;inset:0}
  .dot-grid{position:absolute;left:27px;top:28px}
  .xray-card{position:absolute;background:var(--paper);padding:4px;box-shadow:0 2px 6px rgba(0,0,0,.18)}
  .xray-card .film{width:100%;height:100%}
  .xray-normal{left:220px;top:92px;width:285px;height:326px;transform:rotate(0.8deg)}
  .xray-normal .film{background:radial-gradient(ellipse at 50% 55%, #d9d9d9 0%, #9a9a9a 35%, #3d3d3d 70%, #111 100%)}
  .xray-enlarged{left:488px;top:195px;width:332px;height:452px;transform:rotate(4.5deg)}
  .xray-enlarged .film{background:radial-gradient(ellipse at 48% 55%, #e2e2e2 0%, #a7a7a7 38%, #404040 70%, #0d0d0d 100%)}
  .hanger{position:absolute;overflow:visible}
  .xray-label{position:absolute;font-weight:700;color:var(--ink);letter-spacing:.5px;white-space:nowrap}
  .label-normal{left:264px;top:424px;font-size:19px;transform:rotate(0.8deg)}
  .label-enlarged{left:512px;top:652px;font-size:21px;transform:rotate(3.5deg)}
  .warning-sign{position:absolute;left:672px;top:505px}

  .headline{position:absolute;left:0;top:0;font-weight:400}
  .headline span{position:absolute;white-space:nowrap;display:block}
  .headline .lead{left:45px;top:414px;font-family:'Kaushan Script',cursive;font-size:46px;line-height:1;color:var(--orange);transform:rotate(-4deg)}
  .headline .main{left:33px;top:484px;font-family:'Rubik Dirt',sans-serif;font-size:150px;line-height:1;color:var(--ink);letter-spacing:-3px}
  .headline .sub{left:66px;top:618px;font-family:'Kaushan Script',cursive;font-size:64px;line-height:1;color:var(--orange);transform:rotate(-4deg)}

  .dog-photo{position:absolute;left:560px;top:748px;width:288px;height:418px;
    background:radial-gradient(ellipse at 68% 38%, #c97a3a 0%, rgba(184,116,60,.85) 22%, rgba(220,170,120,.35) 42%, rgba(245,245,245,0) 62%),
               radial-gradient(ellipse at 25% 84%, #6c5a50 0%, rgba(108,90,80,.5) 16%, rgba(245,245,245,0) 32%);}

  .intro{position:absolute;left:37px;top:743px;font-size:13px}
  .symptom-list{position:absolute;list-style:none;color:var(--brown);font-weight:700;font-size:15px}
  .symptom-list li{display:flex;align-items:flex-start;gap:10px;line-height:1.15}
  .symptom-list svg{flex:none;width:19px;height:18px;margin-top:-2px}
  .major-left{left:37px;top:771px}
  .major-left li{height:26.5px}
  .major-right{left:246px;top:771px}
  .major-right li{height:26.5px}
  .note{position:absolute;left:36px;font-size:12.6px;line-height:1.25}
  .note-preclinical{top:879px;width:530px}
  .note-exam{top:920px;width:420px}
  .exam-list{left:37px;top:974px;width:620px;font-size:14.6px}
  .exam-list li{margin-bottom:9px;white-space:nowrap}
</style>
</head>
<body>
<main class="poster">
  <svg class="backdrop" width="848" height="1200" aria-hidden="true">
    <path d="M530 0 H848 V332 C760 320 600 260 520 160 C500 100 510 40 530 0 Z" fill="var(--soft-grey)"/>
    <path d="M0 1035 C80 1030 150 1080 167 1150 C172 1170 170 1190 166 1200 H0 Z" fill="var(--soft-grey)"/>
  </svg>

  <svg class="dot-grid" width="225" height="85" aria-hidden="true" fill="var(--orange)">
    <circle cx="6" cy="6" r="5.5"/><circle cx="30" cy="6" r="5.5"/><circle cx="53" cy="6" r="5.5"/><circle cx="76" cy="6" r="5.5"/><circle cx="98" cy="6" r="5.5"/><circle cx="122" cy="6" r="5.5"/><circle cx="143" cy="6" r="5.5"/><circle cx="167" cy="6" r="5.5"/><circle cx="190" cy="6" r="5.5"/><circle cx="213" cy="6" r="5.5"/>
    <circle cx="6" cy="30" r="5.5"/><circle cx="30" cy="30" r="5.5"/><circle cx="53" cy="30" r="5.5"/><circle cx="76" cy="30" r="5.5"/><circle cx="98" cy="30" r="5.5"/><circle cx="122" cy="30" r="5.5"/><circle cx="143" cy="30" r="5.5"/><circle cx="167" cy="30" r="5.5"/><circle cx="190" cy="30" r="5.5"/>
    <circle cx="6" cy="53" r="5.5"/><circle cx="30" cy="53" r="5.5"/><circle cx="53" cy="53" r="5.5"/><circle cx="76" cy="53" r="5.5"/><circle cx="98" cy="53" r="5.5"/><circle cx="122" cy="53" r="5.5"/><circle cx="143" cy="53" r="5.5"/><circle cx="167" cy="53" r="5.5"/>
    <circle cx="6" cy="76" r="5.5"/><circle cx="30" cy="76" r="5.5"/><circle cx="53" cy="76" r="5.5"/><circle cx="76" cy="76" r="5.5"/><circle cx="98" cy="76" r="5.5"/><circle cx="122" cy="76" r="5.5"/><circle cx="143" cy="76" r="5.5"/>
  </svg>

  <svg class="hanger" style="left:285px;top:15px" width="140" height="80" aria-hidden="true">
    <path d="M4 72 L69 7 L133 76" fill="none" stroke="var(--chain)" stroke-width="2.5" stroke-dasharray="3 1.5"/>
    <circle cx="69" cy="8" r="6" fill="#d4d4d4" stroke="#aaa"/>
  </svg>
  <div class="xray-card xray-normal">
    <div class="film" role="img" aria-label="Chest X-ray of a dog with a normal sized heart"></div>
  </div>
  <p class="xray-label label-normal">NORMAL HEART</p>

  <svg class="hanger" style="left:612px;top:120px" width="140" height="80" aria-hidden="true">
    <path d="M4 64 L68 8 L124 74" fill="none" stroke="var(--chain)" stroke-width="2.5" stroke-dasharray="3 1.5"/>
    <circle cx="68" cy="8" r="6" fill="#d4d4d4" stroke="#aaa"/>
  </svg>
  <div class="xray-card xray-enlarged">
    <div class="film" role="img" aria-label="Chest X-ray of a dog with an enlarged heart"></div>
  </div>
  <svg class="warning-sign" width="152" height="152" viewBox="0 0 152 152" aria-hidden="true">
    <path d="M56 8 L144 100 Q150 112 138 116 L20 140 Q6 142 10 128 Z" fill="none" stroke="var(--orange)" stroke-width="7" stroke-linejoin="round"/>
    <path d="M53 42 L66 41 L71 100 L61 101 Z" fill="var(--orange)"/>
    <rect x="62" y="108" width="12" height="12" fill="var(--orange)" transform="rotate(-4 68 114)"/>
  </svg>
  <p class="xray-label label-enlarged">ENLARGED HEART</p>

  <h1 class="headline">
    <span class="lead">Do you</span>
    <span class="main">FEED</span>
    <span class="sub">Grain-Free?</span>
  </h1>

  <div class="dog-photo" role="img" aria-label="Photo of a sitting ginger and white dog beside a ceramic food bowl"></div>

  <svg width="0" height="0" style="position:absolute" aria-hidden="true">
    <symbol id="paw" viewBox="0 0 20 19">
      <ellipse cx="10" cy="13.5" rx="5.2" ry="4.5" fill="currentColor"/>
      <ellipse cx="3" cy="8" rx="2.3" ry="2.8" fill="currentColor"/>
      <ellipse cx="7" cy="3.5" rx="2.3" ry="3" fill="currentColor"/>
      <ellipse cx="13" cy="3.5" rx="2.3" ry="3" fill="currentColor"/>
      <ellipse cx="17" cy="8" rx="2.3" ry="2.8" fill="currentColor"/>
    </symbol>
  </svg>

  <p class="intro">The major symptoms of DCM include:</p>
  <ul class="symptom-list major-left">
    <li><svg><use href="#paw"/></svg>Lethargy</li>
    <li><svg><use href="#paw"/></svg>Anorexia</li>
    <li><svg><use href="#paw"/></svg>Labored breathing</li>
    <li><svg><use href="#paw"/></svg>Panting</li>
  </ul>
  <ul class="symptom-list major-right">
    <li><svg><use href="#paw"/></svg>Coughing</li>
    <li><svg><use href="#paw"/></svg>Abdominal distension</li>
    <li><svg><use href="#paw"/></svg>Sudden collapse</li>
  </ul>

  <p class="note note-preclinical">In some cases, dogs with preclinical DCM (prior to the appearance of symptoms) may be given a questionable diagnosis if they appear to be in fine health.</p>
  <p class="note note-exam">On the other hand, a thorough physical exam can reveal some of the subtle symptoms of DCM, such as:</p>

  <ul class="symptom-list exam-list">
    <li><svg><use href="#paw"/></svg>Pulse deficits</li>
    <li><svg><use href="#paw"/></svg>Premature heart contractions that originate in or above the ventricles</li>
    <li><svg><use href="#paw"/></svg><span>Slow capillary refill time in the mucous membrane tissues<br>(e.g., gums are slow to turn pink again after pressing on them<br>gently), indicating poor circulation</span></li>
    <li><svg><use href="#paw"/></svg><span>Breathing sounds muffled or crackly due to the presence<br>of fluid in the lungs</span></li>
  </ul>
</main>
</body>
</html>
```